Infectious Diseases Research Laboratory Needs Business Card

We need a business card for an academic research laboratory based in Kansas City called MORVEK. The full lab name is Microbial Dose-Response/Exposure Bridging Studies Laboratory, but this does not need to be incorporated. We study novel ways to optimize the treatment of multidrug-resistant bacterial infections ("superbugs") throughout the entire biomedical research spectrum (from benchtop to bedside). The name MORVEK is not only an acronym for our lab name, but also represents our desire to make discoveries and explore the unknown (the stars, if you well). It also serves as an ode to the state of Kansas motto where we are based, ad astra per aspera ("to the stars, through difficulty").

Target Market(s)

Pharmaceutical companies, researchers

Industry/Entity Type

Pharmaceutical

Contact Information for Business Card

The business card should incorporate and complement our new logo (see uploaded files). Double-sided designs are preferred. Looking for something modern, but professional.

Font styles to use
Sans Serif

Requirements
Must have
• Double-sided. One side would ideally be a solid color incorporating logo and the other should also have the logo (smaller), but incorporate staff information.
• Color codes:
• Red: #F04C51
• Blue: #3477B5
• Gray: #808285

```html
<!DOCTYPE html>
<html lang="en">
<head>
<meta charset="utf-8">
<title>MORVEK Business Card</title>
<link href="https://fonts.googleapis.com/css2?family=Poppins:wght@400;500;600&display=swap" rel="stylesheet">
<style>
  :root {
    --page-bg: #3a3b3d;
    --card-bg: #1c1c1e;
    --red: #f04c51;
    --blue: #3477b5;
    --gray: #808285;
    --gloss: #5a5b5e;
    --white: #f2f2f2;
  }
  * { box-sizing: border-box; margin: 0; padding: 0; }
  html, body {
    width: 800px;
    height: 1200px;
    overflow: hidden;
    background: var(--page-bg);
    font-family: "Poppins", sans-serif;
  }
  .canvas {
    position: relative;
    width: 800px;
    height: 1200px;
  }
  .card {
    position: absolute;
    left: 50px;
    width: 700px;
    height: 400px;
    background: var(--card-bg);
    border-radius: 4px;
    box-shadow: 0 12px 30px rgba(0,0,0,.45);
    overflow: hidden;
  }
  .card--front { top: 110px; }
  .card--back { top: 690px; }

  .front-mark {
    position: absolute;
    inset: 0;
    display: flex;
    align-items: center;
    justify-content: center;
    gap: 18px;
  }
  .front-mark__dot {
    width: 34px;
    height: 34px;
    border-radius: 50%;
    background: var(--gloss);
  }
  .front-mark__name {
    font-weight: 500;
    font-size: 54px;
    letter-spacing: 10px;
    color: var(--gloss);
  }

  .brand {
    position: absolute;
    left: 56px;
    top: 120px;
    width: 240px;
    display: flex;
    flex-direction: column;
    align-items: center;
    gap: 22px;
  }
  .brand__dot {
    width: 64px;
    height: 64px;
    border-radius: 50%;
    background: var(--blue);
  }
  .brand__name {
    font-weight: 500;
    font-size: 50px;
    letter-spacing: 6px;
    color: var(--red);
  }

  .staff {
    position: absolute;
    left: 366px;
    top: 92px;
    color: var(--white);
  }
  .staff__name {
    font-weight: 600;
    font-size: 27px;
    line-height: 1.1;
    color: var(--red);
  }
  .staff__title {
    font-size: 14px;
    margin-top: 2px;
    margin-bottom: 26px;
  }
  .contact {
    list-style: none;
    font-size: 13.5px;
    line-height: 1.4;
  }
  .contact__item {
    display: flex;
    align-items: flex-start;
    gap: 12px;
    margin-bottom: 8px;
  }
  .contact__icon {
    flex: none;
    width: 14px;
    height: 14px;
    margin-top: 3px;
    fill: var(--red);
  }
  .contact__web { color: var(--red); }
</style>
</head>
<body>
<main class="canvas">

  <section class="card card--front" aria-label="Card front">
    <div class="front-mark">
      <span class="front-mark__dot"></span>
      <span class="front-mark__name">MORVEK</span>
    </div>
  </section>

  <section class="card card--back" aria-label="Card back">
    <div class="brand">
      <span class="brand__dot"></span>
      <span class="brand__name">MORVEK</span>
    </div>

    <div class="staff">
      <h1 class="staff__name">Dana Whitlow</h1>
      <p class="staff__title">Principal Investigator</p>
      <ul class="contact">
        <li class="contact__item">
          <svg class="contact__icon" viewBox="0 0 14 14" aria-hidden="true"><path d="M7 0a5 5 0 0 0-5 5c0 3.6 5 9 5 9s5-5.4 5-9a5 5 0 0 0-5-5zm0 7a2 2 0 1 1 0-4 2 2 0 0 1 0 4z"/></svg>
          <span>48 Meridian Avenue<br>Kansas City, MO 64108</span>
        </li>
        <li class="contact__item">
          <svg class="contact__icon" viewBox="0 0 14 14" aria-hidden="true"><path d="M3 0l2.5 3.5-1.5 1.8a8 8 0 0 0 4.7 4.7L10.5 8.5 14 11l-1.6 2.4C6.5 14 0 7.5.6 1.6z"/></svg>
          <span>816-555-0142</span>
        </li>
        <li class="contact__item">
          <svg class="contact__icon" viewBox="0 0 14 14" aria-hidden="true"><path d="M0 2h14v1.2L7 7.6 0 3.2zM0 4.8l7 4.4 7-4.4V12H0z"/></svg>
          <span>d.whitlow@morveklab.org</span>
        </li>
        <li class="contact__item">
          <svg class="contact__icon" viewBox="0 0 14 14" aria-hidden="true"><path d="M7 0a7 7 0 1 0 0 14A7 7 0 0 0 7 0zm0 1.5c.9 0 1.9 2 2.1 4.7H4.9C5.1 3.5 6.1 1.5 7 1.5zM4.9 7.8h4.2C8.9 10.5 7.9 12.5 7 12.5s-1.9-2-2.1-4.7z"/></svg>
          <span class="contact__web">www.morveklab.org</span>
        </li>
      </ul>
    </div>
  </section>

</main>
</body>
</html>
```